New Business Card Design Project

Vorin focus is KLM Asset Management and Supply Chain.
We have Business Process Experts that can help you get the maximum potential out of your KLM T/7ORBA ERP. We look to understand your business and through the People, Process and Technologies to make you streamline your users digital experience.

The back of the card will be either;
- all black with the orange logo
- all orange with the black logo
- all white with the orange logo
- or make something special
The detail side, show me your best designs.
Try having the side a different colour. So if the one side is black the other is white…

Target Market(s)

Corporate Professional Business

Industry/Entity Type

Mining, Software

Contact Information for Business Card

Name, Position, brief what we do

Colors
F0912C
F2A743
F7CA91
FBE8D2
FDF5EE

Requirements
Must have
• Clear Steady Answers to Hard Questions

```html
<!DOCTYPE html>
<html lang="en">
<head>
<meta charset="utf-8">
<title>Vorin Business Card</title>
<link rel="stylesheet" href="https://fonts.googleapis.com/css2?family=Montserrat:wght@600;700&family=Roboto:wght@400;500&display=swap">
<style>
  :root {
    --orange: #f47624;
    --black: #050505;
    --white: #ffffff;
    --stage-top: #d2d2d2;
    --stage-bottom: #9c9c9c;
  }
  * { margin: 0; padding: 0; box-sizing: border-box; }
  html, body { width: 1200px; height: 802px; overflow: hidden; }
  body {
    background: linear-gradient(180deg, var(--stage-top), var(--stage-bottom));
    font-family: "Roboto", Arial, sans-serif;
    position: relative;
  }
  .card {
    position: absolute;
    width: 540px;
    height: 320px;
    border-radius: 26px;
    overflow: hidden;
    box-shadow: 0 18px 36px rgba(0,0,0,0.28);
  }
  .card-front { left: 50px; top: 110px; background: var(--black); color: var(--white); }
  .card-back { left: 610px; top: 372px; background: var(--orange); color: var(--black); }

  .brand {
    position: absolute;
    display: flex;
    align-items: center;
    gap: 12px;
    font-family: "Montserrat", Arial, sans-serif;
    font-weight: 700;
    white-space: nowrap;
  }
  .brand-dot { border-radius: 50%; flex: none; }
  .card-front .brand { right: 60px; top: 52px; font-size: 34px; color: var(--orange); }
  .card-front .brand-dot { width: 44px; height: 44px; background: var(--orange); }
  .card-back .brand { left: 50%; top: 82px; transform: translateX(-50%); font-size: 58px; color: var(--black); }
  .card-back .brand-dot { width: 78px; height: 78px; background: var(--black); }

  .accent-bar { position: absolute; left: 0; top: 196px; width: 12px; height: 40px; background: var(--orange); }
  .person-name {
    position: absolute; left: 38px; top: 168px;
    font-family: "Montserrat", Arial, sans-serif; font-weight: 700;
    font-size: 27px; color: var(--orange); letter-spacing: 0.2px;
    white-space: nowrap;
  }
  .person-role { position: absolute; left: 40px; top: 206px; font-size: 16px; }
  .divider { position: absolute; left: 102px; right: 44px; top: 216px; height: 1px; background: var(--white); }
  .contact-list { position: absolute; left: 40px; top: 236px; list-style: none; }
  .contact-list li { display: flex; align-items: center; gap: 10px; font-size: 16px; height: 23px; white-space: nowrap; }
  .contact-list svg { width: 14px; height: 14px; fill: var(--orange); flex: none; }
  .address { position: absolute; right: 44px; top: 232px; text-align: right; font-size: 15px; line-height: 22px; white-space: nowrap; }

  .tagline {
    position: absolute; left: 0; right: 0; bottom: 46px; text-align: center;
    font-family: "Montserrat", Arial, sans-serif; font-weight: 700; font-size: 24px;
    white-space: nowrap;
  }
</style>
</head>
<body>
  <section class="card card-front">
    <div class="brand"><span class="brand-dot"></span>Vorin</div>
    <span class="accent-bar"></span>
    <h1 class="person-name">Marten Hollis</h1>
    <p class="person-role">Owner</p>
    <span class="divider"></span>
    <ul class="contact-list">
      <li><svg viewBox="0 0 24 24"><path d="M6.6 10.8a15.1 15.1 0 0 0 6.6 6.6l2.2-2.2a1 1 0 0 1 1-.25 11.4 11.4 0 0 0 3.6.57 1 1 0 0 1 1 1V20a1 1 0 0 1-1 1A17 17 0 0 1 3 4a1 1 0 0 1 1-1h3.5a1 1 0 0 1 1 1c0 1.25.2 2.45.57 3.57a1 1 0 0 1-.25 1z"/></svg>555.014.2277</li>
      <li><svg viewBox="0 0 24 24"><path d="M2 5h20v14H2z"/><path d="M3 6l9 7 9-7" fill="none" stroke="#050505" stroke-width="1.6"/></svg>info@vorin.example</li>
      <li><svg viewBox="0 0 24 24"><path d="M12 2a10 10 0 1 0 0 20 10 10 0 0 0 0-20zm-1 17.9A8 8 0 0 1 4.1 10L9 15v1a2 2 0 0 0 2 2zm6.9-2.5A2 2 0 0 0 16 16h-1v-3a1 1 0 0 0-1-1H8v-2h2a1 1 0 0 0 1-1V7h2a2 2 0 0 0 2-2v-.4a8 8 0 0 1 2.9 12.8z"/></svg>www.vorin.example</li>
    </ul>
    <p class="address">88, Harbour Row, Suite 4<br>30215, Northland</p>
  </section>

  <section class="card card-back">
    <div class="brand"><span class="brand-dot"></span>Vorin</div>
    <p class="tagline">Clear Steady Answers to Hard Questions</p>
  </section>
</body>
</html>
```